Offshore Energy Projects Management Consultancy needs a business card design

Logo available. We provide teams to deliver engineering consultancy, project management and delivery teams mainly in the offshore renewables sector. The company is all about bringing the right people to a project to deliver the scope.

The business card will be used for all staff.

The business card should be quite simple, vibrant and uncluttered but convey experience, enthusiasm and integration.

Target Market(s)

Energy Project Developers and Tier 1 construction companies

Contact Information for Business Card

Logo should be on the back of the card. I'm happy for the designer to play with the colour of the logo and background colour.

Front of the card should convey all the must have information in a clear and professional manner but without being overly traditional.

Colors

Designer to choose colors to be used in the design.

Requirements
Must have
• Land Line Tel Number, Mobile Tel Number, Email, business address, web address.

```html
<!DOCTYPE html>
<html lang="en">
<head>
<meta charset="utf-8">
<title>Northquay Projects Group — Business Card</title>
<link rel="stylesheet" href="https://fonts.googleapis.com/css2?family=Lato:wght@400;700;900&display=swap">
<style>
  :root {
    --stage: #2b2b2b;
    --card: #f4f4f4;
    --card-edge: #e3e3e3;
    --brand-blue: #1f7fc6;
    --band-blue: #176aa8;
    --band-blue-dark: #0f5a92;
    --navy: #15306b;
    --ink: #555a60;
    --ink-soft: #6d7278;
    --white: #ffffff;
  }
  * { box-sizing: border-box; margin: 0; padding: 0; }
  html, body { width: 1200px; height: 997px; overflow: hidden; }
  body {
    background: var(--stage);
    font-family: "Lato", sans-serif;
    position: relative;
  }
  .card {
    position: absolute;
    width: 520px;
    height: 300px;
    border-radius: 26px;
    background: linear-gradient(180deg, var(--white), var(--card) 60%, var(--card-edge));
    overflow: hidden;
    box-shadow: 0 18px 40px rgba(0,0,0,.45);
  }
  .card--back { left: 50px; top: 348px; }
  .card--front { left: 630px; top: 348px; }

  .wordmark {
    position: absolute;
    left: 0; right: 0;
    text-align: center;
    font-weight: 900;
    color: var(--brand-blue);
    letter-spacing: .5px;
  }
  .card--back .wordmark { top: 128px; font-size: 30px; }
  .card--front .wordmark { top: 46px; font-size: 27px; }
  .wordmark__dot {
    display: inline-block;
    width: 14px; height: 14px;
    border-radius: 50%;
    background: var(--brand-blue);
    margin-right: 10px;
    vertical-align: 2px;
  }

  .person {
    position: absolute;
    left: 62px; top: 148px;
  }
  .person__name {
    font-weight: 700;
    font-size: 17px;
    color: var(--navy);
    letter-spacing: .5px;
  }
  .person__role {
    font-size: 12px;
    color: var(--ink);
    margin-top: 3px;
  }
  .divider {
    position: absolute;
    left: 262px; top: 116px;
    width: 2px; height: 84px;
    background: linear-gradient(180deg, transparent, var(--band-blue), transparent);
  }
  .contacts {
    position: absolute;
    left: 284px; top: 118px;
    list-style: none;
  }
  .contacts li {
    display: flex;
    align-items: center;
    font-size: 13.5px;
    color: var(--ink-soft);
    height: 24px;
  }
  .contacts svg { width: 13px; height: 13px; margin-right: 12px; fill: var(--band-blue); }
  .band {
    position: absolute;
    left: 0; right: 0; bottom: 0;
    height: 66px;
    background: linear-gradient(180deg, var(--band-blue), var(--band-blue-dark));
    color: var(--white);
    font-size: 15px;
    letter-spacing: .3px;
    display: flex;
    align-items: center;
    justify-content: center;
  }
</style>
</head>
<body>
  <section class="card card--back" aria-label="Card back">
    <div class="wordmark"><span class="wordmark__dot"></span>Northquay Projects Group</div>
  </section>

  <section class="card card--front" aria-label="Card front">
    <div class="wordmark"><span class="wordmark__dot"></span>Northquay Projects Group</div>

    <div class="person">
      <p class="person__name">SELMA DAROUK</p>
      <p class="person__role">CEO</p>
    </div>

    <div class="divider"></div>

    <ul class="contacts">
      <li>
        <svg viewBox="0 0 16 16"><path d="M3 1h3l1.5 4-2 1.2a9 9 0 0 0 4.3 4.3L11 8.5l4 1.5v3c0 1-1 2-2 2C6.9 15 1 9.1 1 3c0-1 1-2 2-2z"/></svg>
        +90 000 555 0142
      </li>
      <li>
        <svg viewBox="0 0 16 16"><path d="M1 3h14v10H1z M1 3l7 6 7-6" fill="none" stroke="#176aa8" stroke-width="1.8"/></svg>
        info@northquay.com
      </li>
      <li>
        <svg viewBox="0 0 16 16"><circle cx="8" cy="8" r="6.5" fill="none" stroke="#176aa8" stroke-width="1.6"/><path d="M1.5 8h13M8 1.5c-3 3.5-3 9.5 0 13M8 1.5c3 3.5 3 9.5 0 13" fill="none" stroke="#176aa8" stroke-width="1.2"/></svg>
        www.northquay.com
      </li>
    </ul>

    <div class="band">12 Rue des Voiliers, Rabat, Morocco</div>
  </section>
</body>
</html>
```